Northgate Baptist Church Banner Design

Designing 6 banners (3 + 3 that will hang on opposite sides of our auditorium) that are 10 feet long by 4 feet wide.

Use our branding guide - specifically item 4 (vertical logo) and item 5 (icon logo).

Design elements found in our ASCEND booklet, we would like to see designs that utilize the white, green and blue colour palettes but NOT the grey. Other colours may be incorporated (e.g. coral).

We are looking for 3 banner designs that would match on either side of the auditorium, the first banner incorporating the word "TRUTH", the second incorporating the word "LOVE", and the third incorporating the word "MISSION".

We interested in incorporating graphics such as trees or outdoor themes.

Font styles to use
Other font styles liked:
• Montserrat

Colors
34a7d7
00a990
f47c35

Requirements
Must have
• Banner Type #1 include the word "TRUTH"
Banner Type #2 include the word "LOVE"
Banner Type #3 include the word "MISSION"

Colour scheme must include CMYK 54 / 5 / 16 / 0 (which is available in the branding guide.) We have selected the three colours, included below in the brief.

From the branding guide - utilize #5 (icon) for the banner.

UPDATE: After reviewing the initial submissions, we are asking for designs that ONLY incorporate #5 - the ICON logo for the banners.
Nice to have
• It would be nice to have some creativity with the colour ... though a more minimalistic style is preferred.

Graphic adaptations such as trees in the background would be of interest.
Should not have
• Colour scheme should not be gray scale.

The banners should NOT be too busy.

Scripture verses (written out) are not necessary.

```html
<!DOCTYPE html>
<html lang="en">
<head>
<meta charset="utf-8">
<title>Northgate Baptist Church Banners</title>
<link href="https://fonts.googleapis.com/css2?family=Montserrat:wght@600;700&display=swap" rel="stylesheet">
<style>
  :root {
    --backdrop: #b8b8b8;
    --banner-white: #ffffff;
    --brand-teal: #6bbfd0;
    --brand-blue: #34a7d7;
    --band-deep-blue: #1d5a6e;
    --canopy-light: #8fd0dd;
  }
  html, body {
    margin: 0;
    padding: 0;
    width: 1200px;
    height: 933px;
    overflow: hidden;
    background: var(--backdrop);
    font-family: "Montserrat", sans-serif;
  }
  .banner-set {
    position: relative;
    width: 1200px;
    height: 933px;
  }
  .banner {
    position: absolute;
    top: 135px;
    width: 262px;
    height: 657px;
    background: var(--banner-white);
    overflow: hidden;
  }
  .banner--truth { left: 135px; }
  .banner--love { left: 475px; }
  .banner--mission { left: 815px; }

  .brand-mark {
    position: absolute;
    top: 34px;
    left: 50%;
    width: 150px;
    height: 150px;
    margin-left: -75px;
    border-radius: 50%;
    background: var(--brand-teal);
  }
  .brand-name {
    position: absolute;
    top: 203px;
    left: 0;
    right: 0;
    text-align: center;
    line-height: 1;
  }
  .brand-name__main {
    display: block;
    color: var(--brand-teal);
    font-weight: 700;
    font-size: 33px;
    letter-spacing: 0.3px;
  }
  .brand-name__sub {
    display: block;
    margin-top: 8px;
    color: var(--band-deep-blue);
    font-weight: 700;
    font-size: 17px;
    letter-spacing: 1.6px;
  }
  .brand-name__place {
    display: block;
    margin-top: 8px;
    color: var(--band-deep-blue);
    font-weight: 600;
    font-size: 9px;
    letter-spacing: 19px;
    padding-left: 19px;
  }

  .value-band {
    position: absolute;
    top: 312px;
    left: 0;
    width: 262px;
    height: 150px;
  }
  .value-band svg {
    position: absolute;
    inset: 0;
    width: 100%;
    height: 100%;
  }
  .value-band__shape { fill: var(--band-deep-blue); }
  .value-word {
    position: absolute;
    inset: 0;
    display: flex;
    align-items: center;
    justify-content: center;
    color: var(--brand-teal);
    font-weight: 700;
    font-size: 50px;
    letter-spacing: 0.3px;
    line-height: 1;
  }
  .banner--mission .value-word { font-size: 48px; }

  .treeline {
    position: absolute;
    left: 0;
    bottom: 0;
    width: 262px;
    height: 140px;
  }
  .treeline svg { display: block; width: 100%; height: 100%; }
</style>
</head>
<body>
  <main class="banner-set">
    <section class="banner banner--truth">
      <div class="brand-mark"></div>
      <div class="brand-name">
        <span class="brand-name__main">NORTHGATE</span>
        <span class="brand-name__sub">BAPTIST CHURCH</span>
        <span class="brand-name__place">ASHBROOK</span>
      </div>
      <div class="value-band">
        <svg viewBox="0 0 262 150" preserveAspectRatio="none" aria-hidden="true">
          <path class="value-band__shape" d="M0 12 L14 9 L26 12 L40 6 L55 10 L70 5 L86 9 L100 4 L118 8 L134 5 L150 9 L166 3 L182 8 L198 5 L214 9 L230 4 L246 8 L262 6 L262 134 L246 137 L230 133 L214 139 L196 135 L180 140 L162 136 L146 141 L128 137 L110 142 L94 138 L76 143 L58 139 L40 144 L22 140 L0 143 Z"/>
        </svg>
        <span class="value-word">TRUTH</span>
      </div>
      <div class="treeline" role="img" aria-label="Silhouette of a row of trees on a gentle hill">
        <svg viewBox="0 0 262 140" preserveAspectRatio="none" aria-hidden="true">
          <defs><linearGradient id="canopy-truth" x1="0" y1="0" x2="0" y2="1"><stop offset="0" stop-color="#8fd0dd"/><stop offset="0.6" stop-color="#6bbfd0"/></linearGradient></defs>
          <path fill="url(#canopy-truth)" d="M0 48 Q35 30 70 42 Q110 18 150 34 Q185 10 225 6 Q248 8 262 18 L262 140 L0 140 Z"/>
        </svg>
      </div>
    </section>

    <section class="banner banner--love">
      <div class="brand-mark"></div>
      <div class="brand-name">
        <span class="brand-name__main">NORTHGATE</span>
        <span class="brand-name__sub">BAPTIST CHURCH</span>
        <span class="brand-name__place">ASHBROOK</span>
      </div>
      <div class="value-band">
        <svg viewBox="0 0 262 150" preserveAspectRatio="none" aria-hidden="true">
          <path class="value-band__shape" d="M0 12 L14 9 L26 12 L40 6 L55 10 L70 5 L86 9 L100 4 L118 8 L134 5 L150 9 L166 3 L182 8 L198 5 L214 9 L230 4 L246 8 L262 6 L262 134 L246 137 L230 133 L214 139 L196 135 L180 140 L162 136 L146 141 L128 137 L110 142 L94 138 L76 143 L58 139 L40 144 L22 140 L0 143 Z"/>
        </svg>
        <span class="value-word">LOVE</span>
      </div>
      <div class="treeline" role="img" aria-label="Silhouette of a row of trees on a gentle hill">
        <svg viewBox="0 0 262 140" preserveAspectRatio="none" aria-hidden="true">
          <defs><linearGradient id="canopy-love" x1="0" y1="0" x2="0" y2="1"><stop offset="0" stop-color="#8fd0dd"/><stop offset="0.6" stop-color="#6bbfd0"/></linearGradient></defs>
          <path fill="url(#canopy-love)" d="M0 48 Q35 30 70 42 Q110 18 150 34 Q185 10 225 6 Q248 8 262 18 L262 140 L0 140 Z"/>
        </svg>
      </div>
    </section>

    <section class="banner banner--mission">
      <div class="brand-mark"></div>
      <div class="brand-name">
        <span class="brand-name__main">NORTHGATE</span>
        <span class="brand-name__sub">BAPTIST CHURCH</span>
        <span class="brand-name__place">ASHBROOK</span>
      </div>
      <div class="value-band">
        <svg viewBox="0 0 262 150" preserveAspectRatio="none" aria-hidden="true">
          <path class="value-band__shape" d="M0 12 L14 9 L26 12 L40 6 L55 10 L70 5 L86 9 L100 4 L118 8 L134 5 L150 9 L166 3 L182 8 L198 5 L214 9 L230 4 L246 8 L262 6 L262 134 L246 137 L230 133 L214 139 L196 135 L180 140 L162 136 L146 141 L128 137 L110 142 L94 138 L76 143 L58 139 L40 144 L22 140 L0 143 Z"/>
        </svg>
        <span class="value-word">MISSION</span>
      </div>
      <div class="treeline" role="img" aria-label="Silhouette of a row of trees on a gentle hill">
        <svg viewBox="0 0 262 140" preserveAspectRatio="none" aria-hidden="true">
          <defs><linearGradient id="canopy-mission" x1="0" y1="0" x2="0" y2="1"><stop offset="0" stop-color="#8fd0dd"/><stop offset="0.6" stop-color="#6bbfd0"/></linearGradient></defs>
          <path fill="url(#canopy-mission)" d="M0 48 Q35 30 70 42 Q110 18 150 34 Q185 10 225 6 Q248 8 262 18 L262 140 L0 140 Z"/>
        </svg>
      </div>
    </section>
  </main>
</body>
</html>
```